Please redesign the attached signage to a larger dimensions 6000mm wide x 3000mm high.

this is for large format digital printing.

Target Market(s)

Clients buying cars from car dealerships

Industry/Entity Type

Digital

Font styles to use
Sans Serif

Colors

Designer to choose colors to be used in the design.

```html
<!DOCTYPE html>
<html lang="en">
<head>
<meta charset="utf-8">
<title>Buy Here Pay Here – Billboard</title>
<link rel="stylesheet" href="https://fonts.googleapis.com/css2?family=Kanit:ital,wght@1,700;1,800&display=swap">
<style>
  :root {
    --page-bg: #2e2e2e;
    --blue-top: #2754b8;
    --blue-mid: #1a3f98;
    --blue-deep: #0c2468;
    --navy: #0b1d5a;
    --grey-light: #f0f0f0;
    --grey-mid: #c9c9c9;
    --grey-dark: #8f8f8f;
    --red: #d5121c;
    --red-dark: #9e0a12;
    --white: #ffffff;
    --vehicle-black: #1c1c1c;
    --vehicle-red: #c4161c;
    --vehicle-silver: #7d837e;
  }
  * { margin: 0; padding: 0; box-sizing: border-box; }
  html, body {
    width: 1200px;
    height: 1000px;
    overflow: hidden;
    background: var(--page-bg);
  }
  .billboard {
    position: absolute;
    left: 20px;
    top: 210px;
    width: 1160px;
    height: 580px;
    border-radius: 10px;
    overflow: hidden;
    background: var(--navy);
    font-family: "Kanit", "Arial Black", sans-serif;
    color: var(--white);
  }
  .headline-band {
    position: absolute;
    inset: 0 0 auto 0;
    height: 160px;
    background: linear-gradient(180deg, var(--blue-top) 0%, var(--blue-mid) 55%, var(--blue-deep) 100%);
    display: flex;
    align-items: center;
    justify-content: center;
  }
  .headline {
    font-style: italic;
    font-weight: 800;
    font-size: 80px;
    letter-spacing: 2px;
    line-height: 1;
    margin-top: -6px;
    text-shadow: 0 3px 4px rgba(0,0,0,0.35);
  }
  .showroom-band {
    position: absolute;
    left: 0;
    right: 0;
    top: 160px;
    height: 250px;
    background: linear-gradient(180deg, var(--grey-light) 0%, var(--grey-mid) 55%, var(--grey-dark) 100%);
  }
  .vehicle-lineup {
    position: absolute;
    left: 30px;
    right: 20px;
    top: 135px;
    height: 270px;
    border-radius: 40px 60px 20px 20px;
    background: linear-gradient(90deg,
      var(--vehicle-black) 0%, #3a3a3a 26%,
      var(--vehicle-red) 32%, #8e0f13 52%,
      #2a2a2a 58%, var(--vehicle-silver) 66%, #5e645f 100%);
    opacity: 0.92;
  }
  .lower-band {
    position: absolute;
    left: 0;
    right: 0;
    top: 410px;
    bottom: 0;
    background: linear-gradient(180deg, var(--blue-deep) 0%, var(--navy) 100%);
  }
  .offer-banner {
    position: absolute;
    left: 140px;
    top: 392px;
    width: 870px;
    height: 92px;
    transform: skewX(-8deg);
    background: var(--white);
    padding: 7px;
    box-shadow: 0 4px 8px rgba(0,0,0,0.4);
  }
  .offer-banner-fill {
    width: 100%;
    height: 100%;
    background: linear-gradient(180deg, var(--red) 0%, var(--red-dark) 100%);
    display: flex;
    align-items: center;
    justify-content: center;
  }
  .offer-text {
    transform: skewX(8deg);
    font-style: italic;
    font-weight: 800;
    font-size: 50px;
    letter-spacing: 1px;
    line-height: 1;
    margin-top: -4px;
  }
  .accepted-list {
    position: absolute;
    left: 20px;
    right: 20px;
    top: 500px;
    height: 60px;
    list-style: none;
    display: flex;
    align-items: center;
    justify-content: space-between;
  }
  .accepted-item {
    display: flex;
    align-items: center;
    gap: 6px;
    font-style: italic;
    font-weight: 700;
    font-size: 29px;
    line-height: 1;
  }
  .tick-icon { width: 46px; height: 46px; flex: none; }
</style>
</head>
<body>
  <main class="billboard">
    <header class="headline-band">
      <h1 class="headline">BUY HERE PAY HERE</h1>
    </header>

    <section class="showroom-band"></section>
    <div class="vehicle-lineup" role="img" aria-label="Illustration of three vehicles: a black pickup truck, a red large SUV and a silver hatchback"></div>

    <section class="lower-band"></section>

    <div class="offer-banner">
      <div class="offer-banner-fill">
        <p class="offer-text">BAD CREDIT? NO PROBLEM!</p>
      </div>
    </div>

    <ul class="accepted-list">
      <li class="accepted-item">
        <svg class="tick-icon" viewBox="0 0 46 46" aria-hidden="true"><circle cx="23" cy="23" r="20" fill="#d5121c" stroke="#fff" stroke-width="3"/><path d="M13 23l7 7 13-14" fill="none" stroke="#fff" stroke-width="5" stroke-linecap="round" stroke-linejoin="round"/></svg>
        Bankruptcy
      </li>
      <li class="accepted-item">
        <svg class="tick-icon" viewBox="0 0 46 46" aria-hidden="true"><circle cx="23" cy="23" r="20" fill="#d5121c" stroke="#fff" stroke-width="3"/><path d="M13 23l7 7 13-14" fill="none" stroke="#fff" stroke-width="5" stroke-linecap="round" stroke-linejoin="round"/></svg>
        Foreclosures
      </li>
      <li class="accepted-item">
        <svg class="tick-icon" viewBox="0 0 46 46" aria-hidden="true"><circle cx="23" cy="23" r="20" fill="#d5121c" stroke="#fff" stroke-width="3"/><path d="M13 23l7 7 13-14" fill="none" stroke="#fff" stroke-width="5" stroke-linecap="round" stroke-linejoin="round"/></svg>
        Repossesion
      </li>
      <li class="accepted-item">
        <svg class="tick-icon" viewBox="0 0 46 46" aria-hidden="true"><circle cx="23" cy="23" r="20" fill="#d5121c" stroke="#fff" stroke-width="3"/><path d="M13 23l7 7 13-14" fill="none" stroke="#fff" stroke-width="5" stroke-linecap="round" stroke-linejoin="round"/></svg>
        Charge Offs
      </li>
    </ul>
  </main>
</body>
</html>
```